Basic business card

use my newly created logo - and the phrases (Lower Cost of Test & Accelarated New Product Introduction) - and my new email domain / ID - use at conferences / tradeshows

Industry/Entity Type

semiconductor

Contact Information for Business Card

Dale J Whitcomb, Owner, communicate via Logo - Lower COT - Cost of Test, Accelerated NPI - New Product Introduction, phone +1 555 014 6208, Chandler, Arizona, USA, dale.whitcomb@vexlora.com

Font styles to use
Sans Serif

Requirements
Nice to have
• re-use my logo created via Pixel Harbor last August (#6182935)

```html
<!DOCTYPE html>
<html lang="en">
<head>
<meta charset="utf-8">
<title>Vexlora Business Card</title>
<link rel="stylesheet" href="https://fonts.googleapis.com/css2?family=Open+Sans:wght@400;700&display=swap">
<style>
  :root {
    --stage: #232323;
    --card: #151515;
    --card-back-top: #1b1b1b;
    --card-back-bottom: #101010;
    --text: #f2f2f2;
    --brand-slate: #56637f;
    --accent-blue: #1178c4;
    --accent-orange: #f7941d;
  }
  * { margin: 0; padding: 0; box-sizing: border-box; }
  html, body {
    width: 1200px; height: 780px; overflow: hidden;
    background: var(--stage);
    font-family: "Open Sans", sans-serif;
  }
  .canvas { position: relative; width: 1200px; height: 780px; }
  .card {
    position: absolute; width: 540px; height: 309px;
    box-shadow: 0 14px 30px rgba(0,0,0,0.55);
    overflow: hidden;
  }
  .card-back {
    left: 60px; top: 70px;
    background: linear-gradient(135deg, var(--card-back-top), var(--card-back-bottom));
  }
  .card-front { left: 600px; top: 400px; background: var(--card); color: var(--text); }

  .brand {
    position: absolute; left: 52px; top: 118px;
    display: flex; align-items: center; gap: 12px;
  }
  .brand-mark { width: 18px; height: 18px; background: var(--brand-slate); }
  .brand-name {
    font-size: 42px; font-weight: 400; letter-spacing: 1px;
    color: var(--brand-slate); line-height: 1;
  }
  .divider {
    position: absolute; left: 300px; top: 52px;
    width: 1px; height: 150px; background: var(--accent-blue);
  }
  .details { position: absolute; left: 322px; top: 48px; }
  .person-name { font-size: 22px; font-weight: 700; line-height: 1.1; }
  .first-name { color: var(--accent-blue); }
  .last-name { color: var(--accent-orange); }
  .person-role { font-size: 12.5px; margin-top: 2px; }
  .contact-list { list-style: none; margin-top: 16px; font-size: 12.5px; line-height: 1.45; }
  .contact-list li { display: flex; align-items: center; gap: 6px; }
  .contact-icon { width: 11px; height: 11px; fill: var(--accent-blue); flex: none; }
  .address { margin-top: 14px; font-size: 12.5px; line-height: 1.4; }
  .stripes { position: absolute; left: 0; bottom: 0; width: 540px; height: 50px; }
</style>
</head>
<body>
<main class="canvas">
  <section class="card card-back" role="img" aria-label="Card back: repeated embossed brand symbol pattern on black"></section>

  <section class="card card-front">
    <div class="brand">
      <span class="brand-mark"></span>
      <span class="brand-name">VEXLORA</span>
    </div>

    <div class="divider"></div>

    <div class="details">
      <p class="person-name"><span class="first-name">Owen</span> <span class="last-name">Hartley</span></p>
      <p class="person-role">Managing Director</p>
      <ul class="contact-list">
        <li>
          <svg class="contact-icon" viewBox="0 0 12 12"><path d="M1 4c0-2 2-3 5-3s5 1 5 3l-2 1-1-1.5H4L3 5z M3 6h6l1 5H2z"/></svg>
          123 456 789
        </li>
        <li>
          <svg class="contact-icon" viewBox="0 0 12 12"><path d="M0 2h12v8H0z" /><path d="M0 2l6 5 6-5" fill="none" stroke="#151515" stroke-width="1.2"/></svg>
          info@yourmail.com
        </li>
        <li>
          <svg class="contact-icon" viewBox="0 0 12 12"><circle cx="6" cy="6" r="5.5"/><path d="M3 3c1 1 2 0 3 1s-1 2 0 3 2 0 2 2" fill="none" stroke="#151515" stroke-width="1"/></svg>
          www.yourwebsite.com
        </li>
      </ul>
      <p class="address">Your address, City<br>State, Zip 1234</p>
    </div>

    <svg class="stripes" viewBox="0 0 540 50" preserveAspectRatio="none" aria-hidden="true">
      <polygon points="0,32 380,32 386,26 386,33 0,40" fill="var(--accent-orange)"/>
      <polygon points="0,44 388,44 392,28 540,28 540,50 0,50" fill="var(--accent-blue)"/>
    </svg>
  </section>
</main>
</body>
</html>
```